Wadi Alsafeer
Wadi Alsafeer - Construction
Creative Brief
Simple
Salem Dabbagh
CEO
Locality 428 - Alley 17 - House 9 Al Dhaheera - Baghdad - Iraq
ceo@wadialsafeer.com
www.wadialsafeer.com
rokba72x rokba72x
i uploaded the final files so you all can work now with it and very soon I'll chose a winner
and i wont you to make these changes in the latter head only: 1- add the address in Arabic language ( محلة 428 - زقاق 17 - دار 9) and 2- change the e-mail into ( info@wadialsafeer.com ) thank you
Hello , great job all i just wont you to add the name and title in English and Arabic language in the businesses cards only, ( name in Arabic : سالم دباغ) and the title(CEO) in Arabic ( المدير المفوض) Regards,

```html
<!DOCTYPE html>
<html lang="en">
<head>
<meta charset="utf-8">
<title>Wadi Alsafeer – Business Card</title>
<link rel="stylesheet" href="https://fonts.googleapis.com/css2?family=Exo+2:wght@400;500;600&display=swap">
<style>
  :root {
    --page: #e9eaec;
    --card: #ffffff;
    --brand-blue: #1e8fe1;
    --swoosh-dark: #55595e;
    --swoosh-light: #c9ccd0;
    --ink-light: #ffffff;
    --ink-soft: #dcefff;
  }
  * { margin: 0; padding: 0; box-sizing: border-box; }
  html, body {
    width: 1200px; height: 901px; overflow: hidden;
    background: var(--page);
    font-family: "Exo 2", sans-serif;
  }
  .business-card {
    position: absolute;
    left: 150px; top: 193px;
    width: 900px; height: 514px;
    background: var(--card);
    border-radius: 46px;
    overflow: hidden;
    box-shadow: 0 10px 30px rgba(0,0,0,0.15);
  }
  .card-waves { position: absolute; inset: 0; }
  .brand-lockup {
    position: absolute;
    right: 70px; top: 120px;
    display: flex; align-items: center; gap: 16px;
    color: var(--brand-blue);
    font-weight: 500;
    font-size: 40px;
    letter-spacing: 1px;
  }
  .brand-square {
    width: 34px; height: 34px;
    background: var(--brand-blue);
  }
  .holder {
    position: absolute;
    left: 48px; top: 300px;
    width: 420px;
    color: var(--ink-light);
    text-align: left;
  }
  .holder-name {
    font-size: 25px; font-weight: 500;
    text-transform: uppercase; letter-spacing: 1px;
    line-height: 1.2;
  }
  .holder-name-ar {
    font-size: 19px; line-height: 1.4;
    text-align: left;
  }
  .holder-title {
    font-size: 16px; color: var(--ink-soft);
    line-height: 1.4;
    display: flex; gap: 8px; align-items: baseline;
  }
  .holder-address {
    margin-top: 22px;
    font-size: 15px; line-height: 1.5;
    color: var(--ink-light);
  }
  .contact-list {
    position: absolute;
    right: 48px; top: 360px;
    list-style: none;
    color: var(--ink-light);
    font-size: 16px;
  }
  .contact-list li {
    display: flex; justify-content: flex-end; align-items: center;
    gap: 10px; height: 27px;
  }
  .contact-list svg { width: 15px; height: 15px; fill: var(--ink-light); }
  .contact-list .gap { height: 14px; }
</style>
</head>
<body>
  <section class="business-card">
    <svg class="card-waves" viewBox="0 0 900 514" preserveAspectRatio="none" aria-hidden="true">
      <path fill="var(--swoosh-light)" d="M0,222 C220,190 390,300 565,292 C720,286 820,228 900,190 C820,238 720,296 565,304 C390,312 220,212 0,236 Z"/>
      <path fill="var(--swoosh-dark)" d="M0,238 C220,205 385,315 565,306 C725,298 825,246 900,212 C830,262 725,316 565,322 C385,330 220,232 0,256 Z"/>
      <path fill="var(--brand-blue)" d="M0,262 C215,240 385,340 565,332 C725,325 830,270 900,236 L900,514 L0,514 Z"/>
    </svg>

    <div class="brand-lockup">
      <span class="brand-square"></span>
      <span class="brand-name">Wadi Alsafeer</span>
    </div>

    <div class="holder">
      <p class="holder-name">Salem Dabbagh</p>
      <p class="holder-name-ar" lang="ar"><bdi dir="rtl">سالم دباغ</bdi></p>
      <p class="holder-title"><span>CEO</span><span>·</span><bdi lang="ar" dir="rtl">المدير المفوض</bdi></p>
      <p class="holder-address">Locality 428 - Alley 17 - House 9<br>Al Dhaheera - Baghdad - Iraq</p>
    </div>

    <ul class="contact-list">
      <li>012 555 0147
        <svg viewBox="0 0 24 24"><path d="M6.6 10.8a15 15 0 0 0 6.6 6.6l2.2-2.2a1 1 0 0 1 1-.25 11 11 0 0 0 3.6.6 1 1 0 0 1 1 1V20a1 1 0 0 1-1 1A17 17 0 0 1 3 4a1 1 0 0 1 1-1h3.5a1 1 0 0 1 1 1 11 11 0 0 0 .6 3.6 1 1 0 0 1-.25 1z"/></svg>
      </li>
      <li>012 555 0148
        <svg viewBox="0 0 24 24"><path d="M7 1h10a2 2 0 0 1 2 2v18a2 2 0 0 1-2 2H7a2 2 0 0 1-2-2V3a2 2 0 0 1 2-2zm0 3v14h10V4zm5 15.5a1 1 0 1 0 0 2 1 1 0 0 0 0-2z"/></svg>
      </li>
      <li>012 555 0149
        <svg viewBox="0 0 24 24"><path d="M6 2h9l3 3v5h1a2 2 0 0 1 2 2v8a2 2 0 0 1-2 2H5a2 2 0 0 1-2-2v-8a2 2 0 0 1 2-2h1zm2 2v6h8V6h-2V4zm-1 9v2h2v-2zm4 0v2h2v-2zm4 0v2h2v-2z"/></svg>
      </li>
      <li class="gap"></li>
      <li>ceo@wadialsafeer.com
        <svg viewBox="0 0 24 24"><path d="M2 5h20v14H2zm2 2v.5l8 5 8-5V7zm0 2.9V17h16V9.9l-8 5z"/></svg>
      </li>
      <li>www.wadialsafeer.com
        <svg viewBox="0 0 24 24"><path d="M12 2a10 10 0 1 0 0 20 10 10 0 0 0 0-20zm0 2c1 1.2 1.8 3 2.1 5H9.9C10.2 7 11 5.2 12 4zM9.7 11h4.6a16 16 0 0 1 0 2H9.7a16 16 0 0 1 0-2zm-5.6 0h3.6a18 18 0 0 0 0 2H4.1a8 8 0 0 1 0-2zm12.2 0h3.6a8 8 0 0 1 0 2h-3.6a18 18 0 0 0 0-2zM9.9 15h4.2c-.3 2-1.1 3.8-2.1 5-1-1.2-1.8-3-2.1-5z"/></svg>
      </li>
    </ul>
  </section>
</body>
</html>
```